High-end construction company needs a business card design

We need a modern looking business card that draws people in, is memorable and looks so good people will want to sick it on their fridges.
On the first side what is needed are:
Logo
My name - Tomas Verbelk
Title - Managing Director
Website - www.kravel.co.uk
Email - tomas@kravel.co.uk
Telephone - 020 5194 6381
Mobile - 07845319027
On the back side was is needed is a list of all the services we provide:
-Kitchen Renovations
-Bathroom Renovations
-House Renovations
-Garage Conversions
-Extensions
-Loft Conversions
-Conservatories
-Carpentry
-Tiling
-Electrical
-Plumbing & Heating
-Bricklaying
-Landscaping
-Decorating
-Plastering
We would like the colours to be the same shades as on the logo with grey or black for the words.
Target Market(s)
Anyone who needs building work done
Contact Information for Business Card
This business card is for a construction company which strives to deliver excellent service and quality.
The look and feel of the card should represent this.
Requirements
Must have
- On the first side what is needed are:
Logo
My name - Tomas Verbelk
Title - Managing Director
Website - www.kravel.co.uk
Email - tomas@kravel.co.uk
Telephone - 020 5194 6381
Mobile - 07845319027
Nice to have
- Cool looking features

```html
<!DOCTYPE html>
<html lang="en">
<head>
<meta charset="utf-8">
<title>Kravel Construction – Business Card</title>
<link href="https://fonts.googleapis.com/css2?family=Montserrat:wght@400;500;700&display=swap" rel="stylesheet">
<style>
  :root {
    --green: #6cbd45;
    --green-deep: #3f9a3c;
    --ink: #141414;
    --charcoal: #2b2b2b;
    --grey-text: #444444;
    --paper: #ffffff;
    --backdrop: #ebebeb;
    --skyline: #b9b9b9;
  }
  * { box-sizing: border-box; margin: 0; padding: 0; }
  html, body {
    width: 686px; height: 1200px; overflow: hidden;
    background: var(--backdrop);
    font-family: "Montserrat", Arial, sans-serif;
  }
  .card {
    position: absolute; left: 43px;
    width: 600px; height: 343px; overflow: hidden;
    box-shadow: 0 6px 18px rgba(0,0,0,.22);
  }
  .card-front { top: 232px; background: var(--paper); }
  .card-back  { top: 625px; background: var(--ink); }
  .card-art { position: absolute; inset: 0; width: 600px; height: 343px; }

  .brand { position: absolute; color: var(--green); font-weight: 700; line-height: 1; }
  .brand-name { display: block; letter-spacing: 1px; }
  .brand-sub  { display: block; letter-spacing: 2.2px; margin-top: 6px; }
  .card-front .brand { left: 50px; top: 118px; }
  .card-front .brand-name { font-size: 44px; }
  .card-front .brand-sub { font-size: 13.4px; }
  .card-back .brand { left: 42px; top: 130px; }
  .card-back .brand-name { font-size: 38px; }
  .card-back .brand-sub { font-size: 11.6px; }

  .person { position: absolute; left: 378px; top: 48px; }
  .person-name { font-size: 22px; font-weight: 700; color: var(--charcoal); letter-spacing: .6px; text-transform: uppercase; }
  .person-name .surname { color: var(--green); }
  .person-title { font-size: 13.5px; color: var(--grey-text); margin-top: 9px; letter-spacing: .3px; }

  .contact-list { position: absolute; list-style: none; }
  .contact-item { display: flex; align-items: center; height: 18px; }
  .contact-icon { width: 18px; height: 18px; flex: none; }
  .contact-text { margin-left: 12px; color: var(--paper); }
  .card-front .contact-list { left: 379px; top: 222px; }
  .card-front .contact-item + .contact-item { margin-top: 5.5px; }
  .contact-text.is-large { font-size: 14.5px; }
  .contact-text.is-small { font-size: 11.5px; }
  .card-back .contact-list { left: 43px; top: 272px; }
  .card-back .contact-item + .contact-item { margin-top: 9px; }
  .card-back .contact-text { color: var(--charcoal); font-size: 13px; margin-left: 11px; }
  .card-back .contact-text.is-small { font-size: 11.5px; }

  .services { position: absolute; left: 242px; top: 33px; color: var(--paper); }
  .services-heading { font-size: 16.5px; font-weight: 400; letter-spacing: .6px; }
  .services-heading strong { color: var(--green); font-weight: 700; }
  .services-rule { width: 27px; height: 1px; background: var(--paper); margin-top: 7px; }
  .services-columns { display: flex; margin-top: 12px; }
  .services-col { list-style: none; }
  .services-col + .services-col { margin-left: 25px; }
  .service { display: flex; align-items: center; height: 24px; font-size: 11.6px; letter-spacing: .2px; }
  .service-tick { width: 12px; height: 12px; margin-right: 12px; flex: none; }
</style>
</head>
<body>

<!-- Front -->
<section class="card card-front" aria-label="Business card front">
  <svg class="card-art" viewBox="0 0 988 565" preserveAspectRatio="none" aria-hidden="false">
    <defs>
      <linearGradient id="skylineFront" x1="0" y1="0" x2="0" y2="1">
        <stop offset="0" stop-color="#cfcfcf"/>
        <stop offset="1" stop-color="#9f9f9f"/>
      </linearGradient>
    </defs>
    <rect role="img" aria-label="Grey city skyline silhouette" x="0" y="390" width="440" height="160" fill="url(#skylineFront)" opacity=".75"/>
    <path d="M560 345 C690 282 850 258 988 330 L988 350 C850 285 700 300 590 342 Z" fill="var(--ink)"/>
    <path d="M0 555 C220 560 430 420 610 352 C760 300 880 315 988 370 L988 565 L0 565 Z" fill="var(--ink)"/>
    <path d="M0 520 C140 545 320 490 450 402 C330 470 160 520 0 502 Z" fill="var(--green-deep)"/>
  </svg>

  <div class="brand">
    <span class="brand-name">KRAVEL</span>
    <span class="brand-sub">CONSTRUCTION LTD</span>
  </div>

  <div class="person">
    <h1 class="person-name">Tomas <span class="surname">Verbelk</span></h1>
    <p class="person-title">Managing Director</p>
  </div>

  <ul class="contact-list">
    <li class="contact-item">
      <svg class="contact-icon" viewBox="0 0 18 18"><circle cx="9" cy="9" r="8.2" fill="none" stroke="var(--green)" stroke-width="1.2"/><path d="M5 7.2 C5 5.6 13 5.6 13 7.2 L11.5 8 L10.8 7 L7.2 7 L6.5 8 Z M6.3 9 L11.7 9 L12.5 12.5 L5.5 12.5 Z" fill="var(--green)"/></svg>
      <span class="contact-text is-large">020 5194 6381</span>
    </li>
    <li class="contact-item">
      <svg class="contact-icon" viewBox="0 0 18 18"><circle cx="9" cy="9" r="8.2" fill="none" stroke="var(--green)" stroke-width="1.2"/><rect x="6.6" y="4.5" width="4.8" height="9" rx="1" fill="none" stroke="var(--green)" stroke-width="1.1"/></svg>
      <span class="contact-text is-large">07845319027</span>
    </li>
    <li class="contact-item">
      <svg class="contact-icon" viewBox="0 0 18 18"><circle cx="9" cy="9" r="8.2" fill="none" stroke="var(--green)" stroke-width="1.2"/><rect x="5" y="6" width="8" height="6" fill="var(--green)"/><path d="M5 6 L9 9.5 L13 6" fill="none" stroke="var(--ink)" stroke-width=".9"/></svg>
      <span class="contact-text is-small">tomas@kravel.co.uk</span>
    </li>
    <li class="contact-item">
      <svg class="contact-icon" viewBox="0 0 18 18"><circle cx="9" cy="9" r="8.2" fill="none" stroke="var(--green)" stroke-width="1.2"/><circle cx="9" cy="9" r="4.2" fill="var(--green)"/><path d="M4.8 9 H13.2 M9 4.8 V13.2 M6.5 6.5 C8 7.8 10 7.8 11.5 6.5 M6.5 11.5 C8 10.2 10 10.2 11.5 11.5" stroke="var(--ink)" stroke-width=".6" fill="none"/></svg>
      <span class="contact-text is-small">www.kravel.co.uk</span>
    </li>
  </ul>
</section>

<!-- Back -->
<section class="card card-back" aria-label="Business card back">
  <svg class="card-art" viewBox="0 0 988 565" preserveAspectRatio="none">
    <defs>
      <linearGradient id="skylineBack" x1="0" y1="0" x2="0" y2="1">
        <stop offset="0" stop-color="#2a2a2a"/>
        <stop offset="1" stop-color="#1c1c1c"/>
      </linearGradient>
    </defs>
    <rect role="img" aria-label="Faint dark city skyline silhouette" x="540" y="380" width="448" height="170" fill="url(#skylineBack)"/>
    <path d="M0 420 C130 375 290 380 400 440 C300 400 150 395 0 435 Z" fill="var(--paper)"/>
    <path d="M0 450 C140 415 300 425 420 470 C580 530 800 560 988 540 L988 565 L0 565 Z" fill="var(--green)"/>
  </svg>

  <div class="brand">
    <span class="brand-name">KRAVEL</span>
    <span class="brand-sub">CONSTRUCTION LTD</span>
  </div>

  <div class="services">
    <h2 class="services-heading">OUR <strong>SERVICES</strong></h2>
    <div class="services-rule"></div>
    <div class="services-columns">
      <ul class="services-col">
        <li class="service"><svg class="service-tick" viewBox="0 0 12 12"><path d="M10.5 4.6 A5 5 0 1 1 8.6 1.6" fill="none" stroke="var(--green)" stroke-width="1"/><path d="M3.6 5.6 L5.6 7.6 L10.8 1.8" fill="none" stroke="var(--green)" stroke-width="1.1"/></svg>Kitchen Renovations</li>
        <li class="service"><svg class="service-tick" viewBox="0 0 12 12"><path d="M10.5 4.6 A5 5 0 1 1 8.6 1.6" fill="none" stroke="var(--green)" stroke-width="1"/><path d="M3.6 5.6 L5.6 7.6 L10.8 1.8" fill="none" stroke="var(--green)" stroke-width="1.1"/></svg>Bathroom Renovations</li>
        <li class="service"><svg class="service-tick" viewBox="0 0 12 12"><path d="M10.5 4.6 A5 5 0 1 1 8.6 1.6" fill="none" stroke="var(--green)" stroke-width="1"/><path d="M3.6 5.6 L5.6 7.6 L10.8 1.8" fill="none" stroke="var(--green)" stroke-width="1.1"/></svg>House Renovations</li>
        <li class="service"><svg class="service-tick" viewBox="0 0 12 12"><path d="M10.5 4.6 A5 5 0 1 1 8.6 1.6" fill="none" stroke="var(--green)" stroke-width="1"/><path d="M3.6 5.6 L5.6 7.6 L10.8 1.8" fill="none" stroke="var(--green)" stroke-width="1.1"/></svg>Garage Conversions</li>
        <li class="service"><svg class="service-tick" viewBox="0 0 12 12"><path d="M10.5 4.6 A5 5 0 1 1 8.6 1.6" fill="none" stroke="var(--green)" stroke-width="1"/><path d="M3.6 5.6 L5.6 7.6 L10.8 1.8" fill="none" stroke="var(--green)" stroke-width="1.1"/></svg>Extensions</li>
        <li class="service"><svg class="service-tick" viewBox="0 0 12 12"><path d="M10.5 4.6 A5 5 0 1 1 8.6 1.6" fill="none" stroke="var(--green)" stroke-width="1"/><path d="M3.6 5.6 L5.6 7.6 L10.8 1.8" fill="none" stroke="var(--green)" stroke-width="1.1"/></svg>Loft Conversions</li>
        <li class="service"><svg class="service-tick" viewBox="0 0 12 12"><path d="M10.5 4.6 A5 5 0 1 1 8.6 1.6" fill="none" stroke="var(--green)" stroke-width="1"/><path d="M3.6 5.6 L5.6 7.6 L10.8 1.8" fill="none" stroke="var(--green)" stroke-width="1.1"/></svg>Conservatories</li>
        <li class="service"><svg class="service-tick" viewBox="0 0 12 12"><path d="M10.5 4.6 A5 5 0 1 1 8.6 1.6" fill="none" stroke="var(--green)" stroke-width="1"/><path d="M3.6 5.6 L5.6 7.6 L10.8 1.8" fill="none" stroke="var(--green)" stroke-width="1.1"/></svg>Carpentry</li>
      </ul>
      <ul class="services-col">
        <li class="service"><svg class="service-tick" viewBox="0 0 12 12"><path d="M10.5 4.6 A5 5 0 1 1 8.6 1.6" fill="none" stroke="var(--green)" stroke-width="1"/><path d="M3.6 5.6 L5.6 7.6 L10.8 1.8" fill="none" stroke="var(--green)" stroke-width="1.1"/></svg>Tiling</li>
        <li class="service"><svg class="service-tick" viewBox="0 0 12 12"><path d="M10.5 4.6 A5 5 0 1 1 8.6 1.6" fill="none" stroke="var(--green)" stroke-width="1"/><path d="M3.6 5.6 L5.6 7.6 L10.8 1.8" fill="none" stroke="var(--green)" stroke-width="1.1"/></svg>Electrical</li>
        <li class="service"><svg class="service-tick" viewBox="0 0 12 12"><path d="M10.5 4.6 A5 5 0 1 1 8.6 1.6" fill="none" stroke="var(--green)" stroke-width="1"/><path d="M3.6 5.6 L5.6 7.6 L10.8 1.8" fill="none" stroke="var(--green)" stroke-width="1.1"/></svg>Plumbing &amp; Heating</li>
        <li class="service"><svg class="service-tick" viewBox="0 0 12 12"><path d="M10.5 4.6 A5 5 0 1 1 8.6 1.6" fill="none" stroke="var(--green)" stroke-width="1"/><path d="M3.6 5.6 L5.6 7.6 L10.8 1.8" fill="none" stroke="var(--green)" stroke-width="1.1"/></svg>Bricklaying</li>
        <li class="service"><svg class="service-tick" viewBox="0 0 12 12"><path d="M10.5 4.6 A5 5 0 1 1 8.6 1.6" fill="none" stroke="var(--green)" stroke-width="1"/><path d="M3.6 5.6 L5.6 7.6 L10.8 1.8" fill="none" stroke="var(--green)" stroke-width="1.1"/></svg>Landscaping</li>
        <li class="service"><svg class="service-tick" viewBox="0 0 12 12"><path d="M10.5 4.6 A5 5 0 1 1 8.6 1.6" fill="none" stroke="var(--green)" stroke-width="1"/><path d="M3.6 5.6 L5.6 7.6 L10.8 1.8" fill="none" stroke="var(--green)" stroke-width="1.1"/></svg>Decorating</li>
        <li class="service"><svg class="service-tick" viewBox="0 0 12 12"><path d="M10.5 4.6 A5 5 0 1 1 8.6 1.6" fill="none" stroke="var(--green)" stroke-width="1"/><path d="M3.6 5.6 L5.6 7.6 L10.8 1.8" fill="none" stroke="var(--green)" stroke-width="1.1"/></svg>Plastering</li>
      </ul>
    </div>
  </div>

  <ul class="contact-list">
    <li class="contact-item">
      <svg class="contact-icon" viewBox="0 0 18 18"><circle cx="9" cy="9" r="8.2" fill="none" stroke="var(--charcoal)" stroke-width="1.2"/><path d="M5 7.2 C5 5.6 13 5.6 13 7.2 L11.5 8 L10.8 7 L7.2 7 L6.5 8 Z M6.3 9 L11.7 9 L12.5 12.5 L5.5 12.5 Z" fill="var(--charcoal)"/></svg>
      <span class="contact-text">020 5194 6381</span>
    </li>
    <li class="contact-item">
      <svg class="contact-icon" viewBox="0 0 18 18"><circle cx="9" cy="9" r="8.2" fill="none" stroke="var(--charcoal)" stroke-width="1.2"/><circle cx="9" cy="9" r="4.2" fill="var(--charcoal)"/><path d="M4.8 9 H13.2 M9 4.8 V13.2 M6.5 6.5 C8 7.8 10 7.8 11.5 6.5 M6.5 11.5 C8 10.2 10 10.2 11.5 11.5" stroke="var(--green)" stroke-width=".6" fill="none"/></svg>
      <span class="contact-text is-small">www.kravel.co.uk</span>
    </li>
  </ul>
</section>

</body>
</html>
```